vLINK ON LLC - New Website Design Help!

Need to build a website that showcases our capabilities. We will be specializing in Government Contracting for SDVOSB set aside and sole source contracts. We provide many services such as Audio & Visual design, install, consulting, all the way through to project completion. Also, IT/Voice infrastructure consulting, design, implementation, project management all the way to project completion.

Target Market(s)

IT/Voice Government Contracts, Managed Service Contracts for Government

Industry/Entity Type

Information Technology and Telecommunications

Coding

Coded - Design and coding required

Number of Pages Required

5+ page

Font styles to use
Other font styles liked:
• Calibri

Colors

Designer to choose only greyscale colors for use in the design.

Requirements
Must have
• Drop downs for additional pages, for About Us, Services, Industry Solutions, Our Company, Contact Us
Nice to have
• Testimonials page or Blog page

```html
<!DOCTYPE html>
<html lang="en">
<head>
<meta charset="utf-8">
<title>vLINK ON LLC – Government Contracting</title>
<link href="https://fonts.googleapis.com/css2?family=Poppins:wght@300;400;500;600;700&family=Fira+Sans:wght@400;500&display=swap" rel="stylesheet">
<style>
:root{
  --black:#0c0c0c;
  --ink:#1b1b1b;
  --muted:#6b6b6b;
  --grey-band:#d6d6d6;
  --grey-light:#efefef;
  --grey-btn:#7a7a7a;
  --white:#ffffff;
  --star:#b9c61b;
}
*{box-sizing:border-box;margin:0;padding:0}
html,body{width:1200px;height:4654px;overflow:hidden}
body{position:relative;font-family:'Poppins',sans-serif;color:var(--ink);background:var(--white)}
.abs{position:absolute}
.brand{font-family:'Poppins',sans-serif;font-weight:600;color:var(--white);font-size:30px;letter-spacing:1px;display:flex;align-items:center;gap:10px}
.brand-square{width:22px;height:22px;background:var(--grey-btn)}
.topbar{left:0;top:0;width:1200px;height:85px;background:var(--black)}
.top-link{color:var(--white);font-size:15px;top:36px}
.search{left:730px;top:31px;width:222px;height:30px;background:var(--white);display:flex}
.search span{flex:1;font-size:13px;color:#aaa;padding:6px 12px}
.search i{width:48px;background:var(--grey-btn)}
.social{top:38px;width:20px;height:20px;border-radius:50%;background:var(--white)}
.nav{left:0;top:85px;width:1200px;height:51px;background:var(--white)}
.nav a{position:absolute;top:16px;font-size:14.5px;font-weight:500;color:var(--ink);text-decoration:none}
.btn{position:absolute;display:flex;align-items:center;justify-content:center;font-size:15px;font-weight:500;color:var(--white);background:var(--grey-btn);letter-spacing:.3px}
.btn.dark{background:var(--black)}
.hero{left:0;top:136px;width:1200px;height:556px;background:linear-gradient(115deg,#3e4147 0%,#5f6670 40%,#8c939c 70%,#6b727a 100%)}
.hero h1{left:33px;top:118px;width:640px;font-size:49px;line-height:53px;color:var(--white);font-weight:700}
.hero p{left:33px;top:289px;width:620px;font-size:14.5px;line-height:26px;color:var(--white)}
.band{left:0;top:692px;width:1200px;height:1455px;background:var(--grey-band)}
.stats{left:193px;top:645px;width:795px;height:166px;background:var(--grey-light)}
.stat{top:48px;display:flex;align-items:center;gap:12px}
.stat b{font-size:50px;font-weight:600;line-height:1;display:block}
.stat small{font-size:14px;color:var(--muted)}
.about-img{left:45px;top:903px;width:535px;height:371px;background:linear-gradient(135deg,#1e3a52,#0f1e2c 55%,#3a4a58)}
.about h2{left:627px;top:955px;font-size:40px;font-weight:600}
.about p{left:631px;width:500px;font-size:12.5px;line-height:23px;color:#333}
.partners{left:33px;top:1353px;width:1129px;height:123px;background:var(--grey-light)}
.badge{top:42px;height:40px;background:#bdbdbd;border-radius:4px}
.svc h3{position:absolute;font-size:25px;font-weight:600;color:var(--ink)}
.svc p{position:absolute;width:295px;font-size:11px;line-height:20px;color:#7a7a7a}
.svc svg{position:absolute}
.expert{left:0;top:2147px;width:1200px;height:713px;background:var(--grey-light)}
.sec-title{position:absolute;left:0;width:1200px;text-align:center;font-size:38px;font-weight:600}
.tile{position:absolute;width:337px;height:225px;display:flex;align-items:flex-end;padding:0 0 16px 17px;font-family:'Fira Sans',sans-serif;font-size:24px;line-height:32px;color:var(--white)}
.testi{left:0;top:2860px;width:1200px;height:555px;background:var(--grey-band)}
.card{position:absolute;top:3039px;width:237px;height:248px;background:var(--white);border-radius:18px;text-align:center}
.card .avatar{width:58px;height:58px;border-radius:50%;background:linear-gradient(#9a9a9a,#5a5a5a);margin:14px auto 0}
.card h4{font-size:15px;font-weight:500;margin-top:8px}
.card p{font-size:10.5px;line-height:17px;color:#555;padding:12px 24px 0}
.card .stars{color:var(--star);font-size:24px;letter-spacing:3px;margin-top:10px}
.post{position:absolute;top:3569px;width:224px;height:318px;background:var(--white);border:1px solid #d0d0d0;text-align:center}
.post .ph{height:159px}
.post h5{font-size:13px;font-weight:600;margin-top:36px}
.post p{font-size:7.5px;line-height:14px;color:#666;padding:10px 18px 0;text-transform:uppercase}
.post .more{font-size:9px;font-weight:600;color:#777;margin-top:12px}
.cta{left:0;top:3961px;width:1200px;height:267px;background:var(--grey-band)}
.footer{left:0;top:4228px;width:1200px;height:426px;background:var(--black);color:var(--white)}
.foot-h{position:absolute;top:93px;font-size:24px;color:#bdbdbd;font-weight:400}
.foot-list{position:absolute;top:150px;list-style:none;font-size:17px;line-height:37px}
.foot-list li::before{content:"›";margin-right:14px;color:#ccc}
.contact-row{position:absolute;left:61px;display:flex;align-items:center;gap:16px;font-size:15px}
</style>
</head>
<body>

<header class="abs topbar">
  <div class="abs brand" style="left:25px;top:24px"><span class="brand-square"></span>vLINK ON LLC</div>
  <span class="abs top-link" style="left:358px">Customer Portal</span>
  <span class="abs top-link" style="left:537px">Support Center</span>
  <div class="abs search"><span>Search Here</span><i></i></div>
  <span class="abs social" style="left:1050px"></span>
  <span class="abs social" style="left:1086px"></span>
  <span class="abs social" style="left:1126px"></span>
</header>

<nav class="abs nav">
  <a style="left:27px">HOME</a><a style="left:119px">ABOUT US</a><a style="left:240px">SERVICES</a>
  <a style="left:367px">INDUSTRY SOLUTIONS</a><a style="left:584px">OUR COMPANY</a>
  <a style="left:743px">TESTIMONIALS</a><a style="left:898px">BLOG</a>
  <span class="btn" style="left:987px;top:9px;width:171px;height:32px">CONTACT US</span>
</nav>

<section class="abs hero" role="img" aria-label="Fighter jet flying above clouds">
  <h1 class="abs">We Are Specializing in Government Contracting for SDVOSB</h1>
  <p class="abs">Lorem ipsum dolor sit amet, consectetur adipiscing elit, sed do eiusmod tempor incididunt ut labore et dolore magna aliqua. Ut enim ad minim veniam, quis nostrud exercitation ullamco laboris nisi ut aliquip ex ea commodo consequat.</p>
  <span class="btn" style="left:33px;top:390px;width:171px;height:32px">CONTACT US</span>
</section>

<div class="abs band"></div>

<div class="abs stats">
  <div class="abs stat" style="left:38px">
    <svg width="66" height="78" viewBox="0 0 66 78" fill="none" stroke="#555" stroke-width="2"><circle cx="33" cy="30" r="24"/><circle cx="33" cy="30" r="16"/><path d="M33 20l3 6 7 1-5 5 1 7-6-3-6 3 1-7-5-5 7-1z"/><path d="M18 48l-8 22 10-4 5 9 6-18M48 48l8 22-10-4-5 9-6-18"/></svg>
    <div><b>20+</b><small>Years Of Experience</small></div>
  </div>
  <div class="abs stat" style="left:300px">
    <svg width="70" height="66" viewBox="0 0 70 66" fill="none" stroke="#555" stroke-width="2"><circle cx="35" cy="24" r="7"/><circle cx="18" cy="34" r="6"/><circle cx="52" cy="34" r="6"/><path d="M24 48c0-8 22-8 22 0v8H24zM6 60c0-8 24-8 24 0M40 60c0-8 24-8 24 0"/><path d="M35 4l2 4 4 .5-3 3 1 4-4-2-4 2 1-4-3-3 4-.5z"/></svg>
    <div><b>500+</b><small>Customers</small></div>
  </div>
  <div class="abs stat" style="left:558px">
    <svg width="76" height="72" viewBox="0 0 76 72" fill="none" stroke="#555" stroke-width="2"><path d="M20 20h26v10c0 10-6 16-13 16S20 40 20 30z"/><path d="M20 24h-8c0 8 4 12 8 12M46 24h8c0 8-4 12-8 12M33 46v10M24 62h18v-6H24z"/><path d="M58 8l10 6M60 20l10-2M52 4l2-4"/></svg>
    <div><b>98%</b><small>Success Score</small></div>
  </div>
</div>

<div class="abs about-img" role="img" aria-label="Developer working at a laptop in front of code screens"></div>
<div class="about">
  <h2 class="abs">ABOUT US</h2>
  <p class="abs" style="top:1018px">Lorem ipsum dolor sit amet, consectetur adipiscing elit, sed do eiusmod tempor incididunt ut labore et dolore magna aliqua. Ut enim ad minim veniam, quis nostrud exercitation ullamco laboris nisi ut aliquip ex ea commodo consequat.</p>
  <p class="abs" style="top:1099px">Lorem ipsum dolor sit amet, consectetur adipiscing elit, sed do eiusmod tempor incididunt ut labore et dolore magna aliqua. Ut enim ad minim veniam, quis nostrud exercitation ullamco laboris nisi ut aliquip ex ea commodo consequat.</p>
  <span class="btn dark" style="left:631px;top:1193px;width:211px;height:32px;font-size:14px">ABOUT OUR COMPANY</span>
</div>

<div class="abs partners">
  <span class="abs badge" style="left:18px;width:146px"></span>
  <span class="abs badge" style="left:205px;width:140px"></span>
  <span class="abs badge" style="left:390px;width:146px"></span>
  <span class="abs badge" style="left:573px;width:146px"></span>
  <span class="abs badge" style="left:766px;width:134px"></span>
  <span class="abs badge" style="left:945px;width:146px"></span>
</div>

<section class="svc">
  <svg style="left:60px;top:1568px" width="72" height="70" viewBox="0 0 72 70" fill="none" stroke="#555" stroke-width="2"><rect x="4" y="4" width="64" height="46"/><rect x="12" y="12" width="48" height="30"/><path d="M30 50l-4 12h20l-4-12M20 64h32"/><circle cx="40" cy="24" r="6"/></svg>
  <h3 style="left:56px;top:1668px">Audio &amp; Visual design</h3>
  <p style="left:56px;top:1710px">Lorem ipsum dolor sit amet, consectetur adipiscing elit, sed do eiusmod tempor incididunt ut labore et dolore magna aliqua.</p>

  <svg style="left:440px;top:1565px" width="84" height="84" viewBox="0 0 84 84" fill="none" stroke="#555" stroke-width="2"><circle cx="42" cy="42" r="30"/><circle cx="42" cy="42" r="18"/><path d="M42 4v8M42 72v8M4 42h8M72 42h8M15 15l6 6M63 63l6 6M15 69l6-6M63 21l6-6"/><circle cx="58" cy="58" r="10"/><path d="M53 58l4 4 6-7"/></svg>
  <h3 style="left:446px;top:1672px">INSTALLATION&nbsp; SERVICES</h3>
  <p style="left:446px;top:1710px">Lorem ipsum dolor sit amet, consectetur adipiscing elit, sed do eiusmod tempor incididunt ut labore et dolore magna aliqua.</p>

  <svg style="left:842px;top:1566px" width="84" height="84" viewBox="0 0 84 84" fill="none" stroke="#555" stroke-width="2"><circle cx="30" cy="30" r="12"/><path d="M14 30a16 16 0 0132 0M14 30v6h4M46 30v6h-4M10 76c0-18 40-18 40 0z"/><rect x="50" y="6" width="30" height="18" rx="3"/><path d="M56 24l-4 6 8-6M56 13h18M56 18h12"/></svg>
  <h3 style="left:838px;top:1668px">24/7 Support</h3>
  <p style="left:838px;top:1710px">Lorem ipsum dolor sit amet, consectetur adipiscing elit, sed do eiusmod tempor incididunt ut labore et dolore magna aliqua.</p>

  <svg style="left:60px;top:1808px" width="70" height="76" viewBox="0 0 70 76" fill="none" stroke="#555" stroke-width="2"><rect x="10" y="4" width="44" height="66"/><rect x="18" y="12" width="28" height="20"/><path d="M28 58V40a4 4 0 018 0v10h8a4 4 0 014 4v16H28z"/></svg>
  <h3 style="left:54px;top:1892px">Access Control</h3>
  <p style="left:54px;top:1934px">Lorem ipsum dolor sit amet, consectetur adipiscing elit, sed do eiusmod tempor incididunt ut labore et dolore magna aliqua.</p>

  <svg style="left:444px;top:1810px" width="76" height="72" viewBox="0 0 76 72" fill="none" stroke="#555" stroke-width="2"><circle cx="26" cy="44" r="20"/><path d="M14 60l-6 8 12-4"/><path d="M22 38a4 4 0 118 0c0 4-4 4-4 8M26 52v2"/><path d="M36 22a20 18 0 1134 10l4 8-10-4a20 18 0 01-20-2"/><path d="M46 20h16M46 26h12"/></svg>
  <h3 style="left:444px;top:1892px">Consulting</h3>
  <p style="left:444px;top:1934px">Lorem ipsum dolor sit amet, consectetur adipiscing elit, sed do eiusmod tempor incididunt ut labore et dolore magna aliqua.</p>

  <svg style="left:836px;top:1804px" width="76" height="72" viewBox="0 0 76 72" fill="none" stroke="#555" stroke-width="2"><rect x="4" y="4" width="44" height="62"/><rect x="10" y="12" width="8" height="8"/><rect x="10" y="28" width="8" height="8"/><rect x="10" y="44" width="8" height="8"/><path d="M22 16h20M22 32h10"/><rect x="30" y="40" width="42" height="28"/><path d="M36 50h8v6h-8zM48 50h8v6h-8zM60 50h8v6h-8z"/></svg>
  <h3 style="left:836px;top:1892px">Project Management</h3>
  <p style="left:836px;top:1934px">Lorem ipsum dolor sit amet, consectetur adipiscing elit, sed do eiusmod tempor incididunt ut labore et dolore magna aliqua.</p>

  <span class="btn" style="left:497px;top:2054px;width:173px;height:35px">CONTACT US</span>
</section>

<section class="abs expert">
  <h2 class="sec-title" style="top:76px">EXPERT SOLUTIONS</h2>
</section>
<div class="tile" style="left:94px;top:2336px;background:linear-gradient(#3f6c95,#14324f)" role="img" aria-label="Blurred office team standing together">Enhanced visibility</div>
<div class="tile" style="left:431px;top:2336px;background:linear-gradient(#34556f,#102436)" role="img" aria-label="Businesswoman in a control room with world map screens">Informed decisions</div>
<div class="tile" style="left:768px;top:2336px;width:336px;background:linear-gradient(#8e959c,#233a52)" role="img" aria-label="Person standing in a foggy city landscape">New business wins</div>
<div class="tile" style="left:94px;top:2561px;background:linear-gradient(#5b7f9d,#1c3b58)" role="img" aria-label="Hands on keyboard with security padlock graphic">Real time performance<br>measurement</div>
<div class="tile" style="left:431px;top:2561px;background:linear-gradient(135deg,#8a3c3c,#27345a 50%,#3e5570)" role="img" aria-label="Business charts and graphs over a city skyline">Increased profitability</div>
<div class="tile" style="left:768px;top:2561px;width:336px;background:linear-gradient(#123456 0,#0c2540 58%,#7a7a7a 58%)" role="img" aria-label="Digital globe with network points">View our solutions<br>&amp; services</div>

<section class="abs testi">
  <h2 class="sec-title" style="top:82px">TESTIMONIALS</h2>
</section>
<div class="card" style="left:181px"><div class="avatar" role="img" aria-label="Client portrait"></div><h4>John Doe</h4><p>Lorem ipsum dolor sit amet, consectetur adipiscing elit, sed do eiusmod tempor incididunt ut labore et dolore magna aliqua.</p><div class="stars">★★★★★</div></div>
<div class="card" style="left:479px"><div class="avatar" role="img" aria-label="Client portrait"></div><h4>John Doe</h4><p>Lorem ipsum dolor sit amet, consectetur adipiscing elit, sed do eiusmod tempor incididunt ut labore et dolore magna aliqua.</p><div class="stars">★★★★★</div></div>
<div class="card" style="left:779px"><div class="avatar" role="img" aria-label="Client portrait"></div><h4>John Doe</h4><p>Lorem ipsum dolor sit amet, consectetur adipiscing elit, sed do eiusmod tempor incididunt ut labore et dolore magna aliqua.</p><div class="stars">★★★★★</div></div>

<h2 class="abs" style="left:74px;top:3472px;font-size:38px;font-weight:600">LATEST FROM BLOG</h2>
<span class="btn dark" style="left:952px;top:3475px;width:172px;height:34px">VIEW ALL</span>
<article class="post" style="left:83px"><div class="ph" role="img" aria-label="Colleagues reviewing data on a laptop" style="background:linear-gradient(#b8c2cc,#4f5d6b)"></div><h5>BLOG POST 1</h5><p>How network audits reveal weak points before they slow down daily operations for agencies</p><div class="more">READ MORE ⟶</div></article>
<article class="post" style="left:358px"><div class="ph" role="img" aria-label="Developer in front of code screens" style="background:linear-gradient(#2a4460,#111d29)"></div><h5>BLOG POST 2</h5><p>Planning voice infrastructure upgrades that keep teams connected across every site</p><div class="more">READ MORE ⟶</div></article>
<article class="post" style="left:632px"><div class="ph" role="img" aria-label="Stealth aircraft on a runway at sunset" style="background:linear-gradient(#d8a070,#3b3f44)"></div><h5>BLOG POST 3</h5><p>Lessons from sole source contracts and what they mean for project delivery timelines</p><div class="more">READ MORE ⟶</div></article>
<article class="post" style="left:907px"><div class="ph" role="img" aria-label="Team meeting around a laptop" style="background:linear-gradient(#c2c9d0,#55616d)"></div><h5>BLOG POST 4</h5><p>Managed services that keep government systems secure and running around the clock</p><div class="more">READ MORE ⟶</div></article>

<section class="abs cta">
  <h2 class="abs" style="left:83px;top:102px;font-size:42px;font-weight:600">24/7 Service and Support!</h2>
  <p class="abs" style="left:83px;top:166px;width:520px;font-size:13.5px;line-height:25px;color:#666">Lorem ipsum dolor sit amet, consectetur adipiscing elit, sed do eiusmod tempor incididunt ut labore et dolore magna aliqua.</p>
  <span class="btn dark" style="left:858px;top:139px;width:217px;height:35px">CONTACT US NOW</span>
</section>

<footer class="abs footer">
  <div class="abs brand" style="left:61px;top:85px"><span class="brand-square"></span>vLINK ON LLC</div>
  <div class="contact-row" style="top:183px"><svg width="20" height="20" viewBox="0 0 20 20" fill="#ccc"><path d="M4 1l4 4-2 3c1 3 3 5 6 6l3-2 4 4-3 3C8 19 1 12 1 4z"/></svg>(+1) 555 014 2260</div>
  <div class="contact-row" style="top:232px"><svg width="20" height="18" viewBox="0 0 20 18" fill="#ccc"><path d="M1 6l9-5 9 5v11H1z"/><path d="M1 6l9 6 9-6" stroke="#000" fill="none"/></svg>support@vlinkon.example</div>
  <div class="contact-row" style="top:281px"><svg width="18" height="22" viewBox="0 0 18 22" fill="#ccc"><path d="M9 0a8 8 0 018 8c0 6-8 14-8 14S1 14 1 8a8 8 0 018-8z"/><circle cx="9" cy="8" r="3" fill="#000"/></svg>210 Harbor Way, Suite 4</div>

  <h3 class="foot-h" style="left:379px">QUICK LINKS</h3>
  <ul class="foot-list" style="left:381px"><li>HOME</li><li>ABOUT</li><li>SERVICES</li><li>PROJECTS</li><li>CONTACT</li></ul>
  <h3 class="foot-h" style="left:638px">SERVICES</h3>
  <ul class="foot-list" style="left:638px"><li>SERVICE 1</li><li>SERVICE 2</li><li>SERVICES</li><li>SERVICE 4</li><li>SERVICE 5</li></ul>
  <h3 class="foot-h" style="left:882px">NEWSLETTER</h3>
  <div class="abs" style="left:882px;top:141px;width:224px;height:33px;display:flex"><span style="flex:1;background:#fff;color:#aaa;font-size:12px;padding:9px 10px">Email Address</span><span style="width:52px;background:var(--grey-btn);font-size:12px;padding:9px 8px">SEND</span></div>
  <span class="abs" style="left:882px;top:230px;width:26px;height:26px;border-radius:50%;background:#ccc"></span>
  <span class="abs" style="left:927px;top:230px;width:26px;height:26px;border-radius:50%;background:#ccc"></span>
  <span class="abs" style="left:974px;top:230px;width:26px;height:26px;border-radius:50%;background:#ccc"></span>

  <span class="abs" style="left:54px;top:387px;font-size:14px">© 2024 | All Rights Reserved.</span>
  <span class="abs" style="left:849px;top:387px;font-size:14px">Terms &amp; Conditions | Privacy Policy</span>
</footer>

</body>
</html>
```